For our product portfolio we need a new packaging design. Our product is a Guaraná-derived energy in powder form. It is sold in small bags, between 350 x 400 mm and 700 x 800 mm, and also in boxes e.g. in the size of 240 x 160 x 45mm.

Our goal is to get creative product design which can be used for
a) the small bags,
b) the boxes, and
c) our Web site logo.

Target Market(s)

Our current target market are computer and Internet geeks. Therefore, we used a LOL-cat in our current/previous design. With the new design we would like to address a broader audience. It would be nice to see logos and packaging designs that are suitable to catch the attention of both geeks as well as normal folks.

Our target audience are people who would buy energy drinks or drink a lot of coffee.

The target audience are young people who work hard and/or go to parties and festivals. The design should be rather playful and funny than serious business.

Industry/Entity Type

Product

Requirements
Must have
• 1. A relationship to the nature product Guaraná. You could, for example, use the red fruits and green leaves of the guarana plant in the design to signal that the product is organic and good for your health. Take a look at http://en.plinthopedia.example/wiki/Guarana for inspirations.
• 2. Our product name is "Velora Fizzpulver"
• 3. The small bags must have certain information in multiple languages (please see image attached as file 1 for reference). We will tell you the specifics when your design is selected as one of our favorites. However, please keep some space in your packaging design for the information text.
• 4. The boxes must have certain information in multiple languages (please see image attached as file 3 for reference). We will tell you the specifics when your design is selected as one of our favorites.
• 5. The graphics must be delivered in an open format so that we can make changes and adjustments after the competition has finished.
• 6. The graphics for packaging must use CMYK colors with at least 600dpi. The logo must use RGB colors with 72dpi.
• Please avoid resemblance with other trademarks, such as Tovimba Borealis.
Nice to have
• A brand identity that is appealing to the "Internet community", e.g. a LOL-cat animal, an Internet meme, or the like.
• Another idea would be to use a hybrid animal, such as http://www.snipmorphs.example/gallery/data/418/medium/stretch_snipmorphs.jpg
• In any case, creative and imaginative submissions are preferred over boring submissions. We are open to all ideas.

```html
<!DOCTYPE html>
<html lang="de">
<head>
<meta charset="utf-8">
<title>Velora Fizzpulver – Beutel</title>
<link rel="stylesheet" href="https://fonts.googleapis.com/css2?family=Quicksand:wght@600&family=Open+Sans:wght@400&display=swap">
<style>
  :root {
    --page: #ffffff;
    --seal: #ececec;
    --seal-line: #d4d4d4;
    --panel: #0a0a0b;
    --panel-edge: #1c1c1e;
    --berry-red: #d3142b;
    --white: #ffffff;
  }
  html, body {
    margin: 0;
    padding: 0;
    width: 958px;
    height: 1200px;
    overflow: hidden;
    background: var(--page);
  }
  .sachet {
    position: absolute;
    left: 130px;
    top: 70px;
    width: 698px;
    height: 1010px;
  }
  .seal {
    position: absolute;
    left: 0;
    width: 100%;
    height: 70px;
    background: repeating-linear-gradient(90deg, var(--seal) 0 9px, var(--seal-line) 9px 11px);
  }
  .seal--top { top: 0; }
  .seal--bottom { bottom: 0; }
  .face {
    position: absolute;
    left: 0;
    top: 70px;
    width: 100%;
    height: 870px;
    background: linear-gradient(90deg, var(--panel-edge), var(--panel) 10%, var(--panel) 90%, var(--panel-edge));
    overflow: hidden;
  }
  .berry-dots {
    position: absolute;
    left: 0;
    top: 20px;
    width: 200px;
    height: 520px;
    background: radial-gradient(ellipse 100% 50% at 0% 50%, rgba(211, 20, 43, 0.9), rgba(211, 20, 43, 0.4) 50%, rgba(211, 20, 43, 0) 100%);
  }
  .fizz-dots {
    position: absolute;
    right: 0;
    top: 400px;
    width: 170px;
    height: 420px;
    background: radial-gradient(ellipse 100% 50% at 100% 55%, rgba(255, 255, 255, 0.9), rgba(255, 255, 255, 0.35) 50%, rgba(255, 255, 255, 0) 100%);
  }
  .brand-name {
    margin: 0;
    font-weight: inherit;
  }
  .wordmark {
    position: absolute;
    font-family: "Quicksand", sans-serif;
    font-weight: 600;
    line-height: 1;
    white-space: nowrap;
    writing-mode: vertical-rl;
    transform: rotate(180deg);
    letter-spacing: -1px;
  }
  .wordmark--velora {
    left: 262px;
    bottom: 150px;
    font-size: 120px;
    color: var(--berry-red);
  }
  .wordmark--fizzpulver {
    left: 382px;
    bottom: 230px;
    font-size: 112px;
    color: var(--white);
  }
  .contents-note {
    position: absolute;
    left: 0;
    width: 100%;
    top: 770px;
    margin: 0;
    text-align: center;
    font-family: "Open Sans", sans-serif;
    font-size: 28px;
    color: var(--white);
  }
</style>
</head>
<body>
  <div class="sachet">
    <div class="seal seal--top"></div>
    <section class="face">
      <div class="berry-dots" role="img" aria-label="Red guaraná-berry halftone dots spreading in from the left edge"></div>
      <div class="fizz-dots" role="img" aria-label="White fizz-bubble halftone dots spreading in from the right edge"></div>
      <h1 class="brand-name">
        <span class="wordmark wordmark--velora">velora</span>
        <span class="wordmark wordmark--fizzpulver">fizzpulver</span>
      </h1>
      <p class="contents-note">Enthält Guaraná</p>
    </section>
    <div class="seal seal--bottom"></div>
  </div>
</body>
</html>
```